Brightwell Standard Procedures and Policy Documents

The Document to work on is Brightwell Policy and Procedure Document, it must flow in the strict order with the photos to follow as we are asking our internal technician team to follow these company policies.

This is more of α technical document so please follow the order I have written in for internal use for clear instructions for our technicians to follow.

Please refer to the Document Brightwell Policy and Procedures * This is the document that needs to be created into α Professional Policy Document,

The titles ,must be included in order and the photos I have placed on there as these are clear instructions for the technicians to follow .

Thanks very much

Colors
3276b5
f68e4d
f04a50

```html
<!DOCTYPE html>
<html lang="en">
<head>
<meta charset="utf-8">
<title>Brightwell Standard Procedures and Policies</title>
<link href="https://fonts.googleapis.com/css2?family=Arvo:ital,wght@0,400;0,700;1,700&family=Arimo:wght@400;700&display=swap" rel="stylesheet">
<style>
:root{
  --navy:#1c3c78;
  --accent:#ee4e23;
  --ink:#2b2b2b;
  --board:#d2d3d5;
  --panel:#f3f4f6;
  --page:#ffffff;
  --link:#2f6db3;
}
*{margin:0;padding:0;box-sizing:border-box}
html,body{width:927px;height:1200px;overflow:hidden}
body{background:var(--board);position:relative;font-family:"Arvo",serif;color:var(--ink)}
.page{position:absolute;width:366px;height:473px;background:var(--page);overflow:hidden}
.page--cover{left:77px;top:90px}
.page--photo{left:482px;top:90px}
.page--standards{left:77px;top:612px}
.page--kit{left:482px;top:612px}
.edge{position:absolute;left:0;right:0;height:6px;background:var(--navy)}
.edge--top{top:0}.edge--bottom{bottom:0}

.brand{position:absolute;display:flex;align-items:center;font-family:"Arvo",serif;color:var(--navy);white-space:nowrap}
.brand__dot{border-radius:50%;background:var(--navy);margin-right:5px}
.brand--large{left:0;right:0;top:50px;justify-content:center;font-size:27px}
.brand--large .brand__dot{width:20px;height:20px;margin-right:8px}
.brand--small{font-size:9px}
.brand--small .brand__dot{width:10px;height:10px;margin-right:3px}
.brand--mid{font-size:13px}
.brand--mid .brand__dot{width:16px;height:16px;margin-right:4px}

.cover-band{position:absolute;left:0;right:0;top:124px;height:72px;background:var(--navy);color:var(--accent);text-align:center;font-size:19px;font-weight:400;line-height:24px;padding-top:12px}
.cover-panel{position:absolute;left:0;right:0;top:196px;height:196px;background:var(--panel);text-align:center;font-size:11.3px;line-height:13.7px;padding:22px 58px 0}
.cover-panel em{color:var(--accent);font-weight:700}
.cover-panel p+p{margin-top:13px}

.contact{position:absolute;display:flex;align-items:center;white-space:nowrap;color:#444}
.contact__icon{display:inline-flex;align-items:center;justify-content:center;background:var(--accent);border-radius:3px}
.contact__icon svg{display:block}
.contact__item{display:flex;align-items:center}
.contact--cover{left:40px;top:430px;font-size:7px}
.contact--cover .contact__icon{width:14px;height:14px;margin-right:6px}
.contact--cover .contact__item+.contact__item{margin-left:10px}
.contact--small{font-size:4.3px}
.contact--small .contact__icon{width:8px;height:8px;margin-right:4px}
.contact--small .contact__item+.contact__item{margin-left:7px}

.title{position:absolute;color:var(--accent);font-weight:400;line-height:25px;font-size:19px;white-space:nowrap}
.title--photo{font-size:17.5px;line-height:24px}
.body{position:absolute;font-family:"Arvo",serif;font-size:6.6px;line-height:8.6px;color:#333}
.body--accent{color:var(--accent)}
.body a{color:var(--link);text-decoration:none}

.photo{position:absolute}
.spec{position:absolute;font-family:"Arimo",sans-serif;color:#222}
.spec__code{font-weight:700;font-size:7px}
.spec__text{font-size:3.6px;line-height:5px;margin-top:6px}
.spec__note{font-size:3.4px;font-style:italic;font-weight:700;margin-top:4px}
.badge{position:absolute;border-radius:4px}
.helper{position:absolute;font-size:6.6px;line-height:8.6px;color:#222}
</style>
</head>
<body>

<section class="page page--cover">
  <div class="brand brand--large"><span class="brand__dot"></span>Brightwell</div>
  <h1 class="cover-band">Brightwell Standard<br>Procedures and Policies.</h1>
  <div class="cover-panel">
    <p>As a highly professional service provider the following policies have been implemented to ensure our Customers receive a Service <em>that is driven by our core values:</em> Quality, Positive Energy, A Reliable Service Provider, Technically Competent, Professional and adhering to Safe Work Standards.</p>
    <p>We thank you for upholding our Values and Strong Work Ethic as a part of the Brightwell Team.</p>
  </div>
  <div class="contact contact--cover">
    <span class="contact__item"><span class="contact__icon"><svg width="8" height="6" viewBox="0 0 8 6"><rect x=".5" y=".5" width="7" height="5" fill="none" stroke="#fff" stroke-width="1"/><path d="M.5 .5L4 3.2 7.5 .5" fill="none" stroke="#fff" stroke-width="1"/></svg></span>Email : service@brightwell.com.au</span>
    <span class="contact__item"><span class="contact__icon"><svg width="8" height="8" viewBox="0 0 8 8"><path d="M1.5 1c.6-.5 1.3-.4 1.6.2l.5 1c.2.4 0 .8-.3 1l-.4.3c.4.9 1 1.5 1.9 1.9l.3-.4c.2-.3.6-.5 1-.3l1 .5c.6.3.7 1 .2 1.6C6 8 4.5 7.6 3 6.2 1.4 4.7 .9 2 1.5 1z" fill="#fff"/></svg></span>HEAD OFFICE: 1300 555 014</span>
  </div>
</section>

<section class="page page--photo">
  <div class="edge edge--top"></div>
  <h2 class="title title--photo" style="left:29px;top:32px">Standard FL2 Photo Verification<br>Reporting</h2>
  <p class="body" style="left:30px;top:86px">FL2 Brightwell Clear Photo Tracking Example - Standard Operating Procedures.</p>
  <p class="body" style="left:30px;top:103px">a) On Arrival to customer site machine photo<br>b) Cleaning of pump photo<br>c) Cleaning of syrup line photo<br>d) Sanitising through the hoppers to check the flow is running well<br>e) Machine photo with product fully " Tested "</p>
  <p class="body" style="left:30px;top:154px;width:310px">Noted &nbsp;# On Completion of Training, 2 Full Hours is required to be spent on the machine as per customer service agreements in place when focused on the machine independently.</p>
  <p class="body" style="left:30px;top:180px">Clear photo example below which are completed to a quality Brightwell Standard.<br>Thanks very much for the follow through your end.</p>
  <p class="body body--accent" style="left:30px;top:206px">Do you need help or assistance ?<br>Any questions pls let us know on email service@brightwell.com.au</p>

  <div class="photo" role="img" aria-label="Machine on arrival at the customer site" style="left:33px;top:236px;width:77px;height:93px;background:linear-gradient(160deg,#7d7f83,#c4c7cb)"></div>
  <div class="photo" role="img" aria-label="Pump being cleaned in a steel sink" style="left:137px;top:236px;width:77px;height:93px;background:linear-gradient(160deg,#5e5a55,#b9b6b0)"></div>
  <div class="photo" role="img" aria-label="Pump assembly in a white bucket" style="left:241px;top:236px;width:77px;height:93px;background:linear-gradient(160deg,#d8d6d2,#8a8f96)"></div>
  <div class="photo" role="img" aria-label="Syrup lines being cleaned" style="left:33px;top:339px;width:77px;height:93px;background:linear-gradient(160deg,#c9c7c3,#6d6a66)"></div>
  <div class="photo" role="img" aria-label="Machine tested with product" style="left:137px;top:339px;width:77px;height:93px;background:linear-gradient(160deg,#3a3b3e,#8c8d90)"></div>
  <div class="photo" role="img" aria-label="Hopper parts sanitised on a rack" style="left:241px;top:339px;width:77px;height:93px;background:linear-gradient(160deg,#e6e0cf,#9a958a)"></div>

  <div class="brand brand--small" style="left:24px;top:450px"><span class="brand__dot"></span>Brightwell</div>
  <div class="contact contact--small" style="left:175px;top:451px">
    <span class="contact__item"><span class="contact__icon"><svg width="5" height="4" viewBox="0 0 8 6"><rect x=".5" y=".5" width="7" height="5" fill="none" stroke="#fff"/><path d="M.5 .5L4 3.2 7.5 .5" fill="none" stroke="#fff"/></svg></span>Email : service@brightwell.com.au</span>
    <span class="contact__item"><span class="contact__icon"><svg width="5" height="5" viewBox="0 0 8 8"><path d="M1.5 1c.6-.5 1.3-.4 1.6.2l.5 1c.2.4 0 .8-.3 1l-.4.3c.4.9 1 1.5 1.9 1.9l.3-.4c.2-.3.6-.5 1-.3l1 .5c.6.3.7 1 .2 1.6C6 8 4.5 7.6 3 6.2 1.4 4.7 .9 2 1.5 1z" fill="#fff"/></svg></span>HEAD OFFICE: 1300 555 014</span>
  </div>
  <div class="edge edge--bottom"></div>
</section>

<section class="page page--standards">
  <div class="edge edge--top"></div>
  <h2 class="title" style="left:29px;top:32px">Standard Time Sheet Reporting</h2>
  <p class="body" style="left:29px;top:62px;width:305px">All Team Members please note the Brightwell policy for processing TimeSheets are due first up Friday mornings by 12pm, this is to ensure Head Office has sufficient time to have the time sheets approved and double checked for Mondays' efficient payroll run.<br>Timesheets are submitted to: &nbsp;<a>service@brightwell.com.au</a></p>
  <h2 class="title" style="left:29px;top:111px">Standard Timely Responses to<br>email and phone</h2>
  <p class="body" style="left:29px;top:166px;width:305px">As we are a Professional Service Provider Company we request that you follow up efficiently to emails and phone calls so we can revert to our Customers with a sense of urgency and timeliness. Thanks very much for your prompt follow up your end in returning calls to Head Office in a timely manner.</p>
  <h2 class="title" style="left:29px;top:214px">Standard Uniform Requirement</h2>
  <p class="body" style="left:29px;top:246px;width:305px">Presenting as a professional Service Agent to build a positive impression with the customer is important to the Brightwell Brand. Please see the clear example of dress to impress the customer as per below. Pls check your grooming standards are neat and tidy.</p>

  <div class="photo" role="img" aria-label="Technician in navy work shirt" style="left:61px;top:289px;width:143px;height:147px;background:linear-gradient(180deg,#f4f4f4 0%,#e6e8ec 40%,#2c3550 100%)"></div>
  <div class="spec" style="left:226px;top:290px;width:60px">
    <div class="spec__code">UW-01</div>
    <p class="spec__text">Pure cotton shirt in a light breathable twill, curved back hem, two front pockets with button flaps, wide back yoke with hidden cooling vents, two piece collar, full button opening and adjustable cuffs.</p>
    <p class="spec__note">Refer below for product colours and sizes</p>
  </div>
  <div class="badge" style="left:226px;top:378px;width:26px;height:26px;background:#6d3fa0"></div>
  <div class="badge" style="left:256px;top:378px;width:26px;height:26px;background:#f4e400"></div>
  <div class="badge" style="left:226px;top:407px;width:26px;height:26px;background:#3aa655"></div>

  <div class="brand brand--small" style="left:24px;top:450px"><span class="brand__dot"></span>Brightwell</div>
  <div class="contact contact--small" style="left:175px;top:451px">
    <span class="contact__item"><span class="contact__icon"><svg width="5" height="4" viewBox="0 0 8 6"><rect x=".5" y=".5" width="7" height="5" fill="none" stroke="#fff"/><path d="M.5 .5L4 3.2 7.5 .5" fill="none" stroke="#fff"/></svg></span>Email : service@brightwell.com.au</span>
    <span class="contact__item"><span class="contact__icon"><svg width="5" height="5" viewBox="0 0 8 8"><path d="M1.5 1c.6-.5 1.3-.4 1.6.2l.5 1c.2.4 0 .8-.3 1l-.4.3c.4.9 1 1.5 1.9 1.9l.3-.4c.2-.3.6-.5 1-.3l1 .5c.6.3.7 1 .2 1.6C6 8 4.5 7.6 3 6.2 1.4 4.7 .9 2 1.5 1z" fill="#fff"/></svg></span>HEAD OFFICE: 1300 555 014</span>
  </div>
  <div class="edge edge--bottom"></div>
</section>

<section class="page page--kit">
  <div class="edge edge--top"></div>
  <div class="photo" role="img" aria-label="Two team members in navy uniform polos outdoors" style="left:27px;top:37px;width:147px;height:135px;background:linear-gradient(180deg,#c9b48a 0%,#a89a7e 45%,#24304f 100%)"></div>
  <div class="photo" role="img" aria-label="Navy work pants with reflective tape" style="left:186px;top:40px;width:72px;height:132px;background:linear-gradient(180deg,#1d2740,#2a3552 85%,#9c9c9c)"></div>
  <div class="spec" style="left:290px;top:52px;width:52px">
    <div class="spec__code">UW-02</div>
    <p class="spec__text">Heavy cotton drill work pants, pre-shrunk, two slant front pockets, one coin pocket, two back pockets with flaps, belt loops and zip fly, reinforced seams at stress points and reflective tape.</p>
    <p class="spec__note">Refer below for product colours and sizes</p>
  </div>
  <div class="badge" style="left:290px;top:128px;width:24px;height:18px;background:#e11d24;border-radius:2px"></div>
  <div class="badge" style="left:317px;top:124px;width:21px;height:21px;background:#f4e400"></div>

  <p class="helper" style="left:26px;top:189px">Double Checking your Tools are all clean and organised. Pls double check you have a Clean<br>drop cloth for underneath your feet while working on customer sites.</p>
  <div class="photo" role="img" aria-label="Clean buckets and brushes laid out on a drop cloth" style="left:26px;top:215px;width:314px;height:206px;background:linear-gradient(180deg,#5a3a2e 0%,#3c4b86 45%,#1c2330 100%)"></div>

  <div class="brand brand--mid" style="left:26px;top:436px"><span class="brand__dot"></span>Brightwell</div>
  <p class="helper" style="left:154px;top:430px">Need any assistance of help ? Running low in stock.<br>Brightwell Head Office is Happy to Assist;</p>
  <div class="contact contact--small" style="left:154px;top:451px">
    <span class="contact__item"><span class="contact__icon"><svg width="5" height="4" viewBox="0 0 8 6"><rect x=".5" y=".5" width="7" height="5" fill="none" stroke="#fff"/><path d="M.5 .5L4 3.2 7.5 .5" fill="none" stroke="#fff"/></svg></span>Email : service@brightwell.com.au</span>
    <span class="contact__item"><span class="contact__icon"><svg width="5" height="5" viewBox="0 0 8 8"><path d="M1.5 1c.6-.5 1.3-.4 1.6.2l.5 1c.2.4 0 .8-.3 1l-.4.3c.4.9 1 1.5 1.9 1.9l.3-.4c.2-.3.6-.5 1-.3l1 .5c.6.3.7 1 .2 1.6C6 8 4.5 7.6 3 6.2 1.4 4.7 .9 2 1.5 1z" fill="#fff"/></svg></span>HEAD OFFICE: 1300 555 014</span>
  </div>
  <div class="edge edge--bottom"></div>
</section>

</body>
</html>
```